New design for 4 homepage screens (no full design) --> Follow-up business for winner

- Please make sure to read these instructions and the PowerPoint File attached
- Varnoki.com is a Swiss-based online store selling business shirts and accessories for business men
- Please visit the page to make yourself familiar with the company. Although the text is in German, with Google translator you should be able to understand the main content.
- Our clients are mainly business men between 30 and 60 years old. Mostly with a high income working in the service industry (banking, insurance, lawyers, etc.). Sometimes there wives purchase the shirts for them ;-)
- The store is based on Crateloom, so you cannot change the layout freely
- The colors and the logo are given, as they are also used for the print materials (please see files in attachment)
- I am running several business and often need a talented web designer --> the winner gets substantial follow-up business

- Your tasks:
- Please design the four screens you can use in the carousel on the homepage
- The design we use today did not receive good enough feedback
- You are free to use graphic elements or (stock) photos (real or Photoshoped). If you are using photos, they must be properly licensed. If license cost are above US$ 100 please check with me in advance.
- Please make sure the text is not too boring, it is OK, if it is a bit hard to read, not all words same size, different alignment or something like this.
- In the attached file, you can find the text that needs to be on the screens. You do not need to use bullet points or stick to the colors, they are just for illustration purposes.
- The Englisch translation on the right-hand side, is just for you – please use the German texts in you design proposals
- At the end of the day, the conversion is key – so first you need to make sure visitors don’t just jump off the page after their first impression and that they browse to the shop. You can use links to connect with other pages (see current version)

Target Market(s)

Men's business shirts and accessoiries

Industry/Entity Type

Business

Number of Pages Required

4 page

Font styles to use
Other font styles liked:
• Presto

Requirements
Must have
• - Match to the existing logo and colors
• - Fit with target audience (business men 30-60 years old)
Nice to have
• Fits with the key terms of our brand:
• - Successful in your job
• - Performance oriented
• - Fast, simple, easy

```html
<!DOCTYPE html>
<html lang="de">
<head>
<meta charset="utf-8">
<title>Varnoki – Business-Hemden und Accessoires</title>
<link rel="stylesheet" href="https://fonts.googleapis.com/css2?family=Open+Sans:wght@400;600;700;800&display=swap">
<style>
:root{
  --gold:#e2ad2f;
  --ink:#222222;
  --muted:#777777;
  --line:#e4e4e4;
  --nav:#151515;
  --footer:#0d0d0d;
  --red:#e0302a;
  --hero-a:#f1f1f1;
  --hero-b:#d6d6d6;
  --bg:#ffffff;
}
*{box-sizing:border-box;margin:0;padding:0}
html,body{width:1200px;height:2816px;overflow:hidden;background:var(--bg);font-family:"Open Sans",Arial,sans-serif;color:var(--ink)}
.page{position:relative;width:1200px;height:2816px}

/* top bar */
.topbar{height:48px;border-bottom:1px solid var(--line);display:flex;align-items:center;justify-content:space-between;padding:0 32px;font-size:11px;color:var(--muted)}
.topbar .like{display:flex;align-items:center;gap:6px;background:#4a68ad;color:#fff;font-size:10px;font-weight:600;padding:3px 8px;border-radius:2px}
.topbar .tools{display:flex;gap:12px;align-items:center}
.topbar .tools svg{width:14px;height:14px;stroke:#555;fill:none;stroke-width:2}

/* brand */
.brand{height:120px;display:flex;flex-direction:column;align-items:center;justify-content:center;gap:8px}
.brand .mark{width:34px;height:34px;background:var(--gold)}
.brand .name{font-size:34px;font-weight:700;letter-spacing:4px;color:var(--gold)}

/* nav */
.mainnav{height:32px;background:var(--nav);display:flex;justify-content:center;align-items:center;gap:34px}
.mainnav a{color:#fff;font-size:11px;font-weight:600;letter-spacing:1px;text-decoration:none}
.mainnav a.active{color:var(--gold)}

/* hero */
.hero{position:relative;height:600px;background:linear-gradient(90deg,var(--hero-a),var(--hero-b))}
.hero .photo{position:absolute;left:70px;top:0;width:420px;height:600px;background:linear-gradient(180deg,#c9c9c9 0%,#2e3f8c 38%,#31418f 62%,#e9e5dc 100%)}
.hero .copy{position:absolute;left:606px;top:348px}
.hero h1{font-size:46px;font-weight:700;letter-spacing:2px;color:#2a2a2a;margin-bottom:22px}
.hero ul{list-style:none}
.hero li{display:flex;align-items:center;gap:14px;font-size:19px;color:#333;margin-bottom:14px}
.hero li::before{content:"";width:18px;height:18px;border-radius:50%;background:#8d8d8d;border:4px solid #bdbdbd}
.hero .cta{display:inline-block;margin-top:14px;background:var(--red);color:#fff;font-size:16px;font-weight:600;padding:10px 22px;text-decoration:none}

/* product rows */
.category{position:absolute;left:0;width:1200px}
.category h2{text-align:center;font-size:22px;font-weight:700;letter-spacing:3px;color:#333}
.row{position:relative;display:grid;grid-template-columns:repeat(6,165px);gap:18px;width:1098px;margin:36px auto 0}
.arrow{position:absolute;top:0;width:20px;height:20px;stroke:#666;fill:none;stroke-width:3}
.product .img{width:165px}
.product .tag{font-size:8px;font-weight:700;color:#555;text-transform:uppercase;margin-top:14px}
.product .title{font-size:9px;font-weight:700;text-transform:uppercase;line-height:13px;margin-top:4px;color:#333}
.product .price{font-size:9px;color:var(--muted);margin-top:8px}
.shirts .img{height:210px;background:linear-gradient(180deg,#fafafa,#e4e6ea)}
.shirts .img.blue{background:linear-gradient(180deg,#dbe7f6,#b6cbe6)}
.shirts .img.sky{background:linear-gradient(180deg,#e7eef8,#cad7ea)}
.ties .img{height:200px;background:#fff;display:flex;justify-content:center}
.ties .img span{display:block;width:40px;height:200px}
.ties .img.sq span{width:120px;height:120px;margin-top:40px}
.links .img{height:70px;background:linear-gradient(90deg,#cfcfcf,#9a9a9a)}
.belts .img{height:80px;margin-top:0}

/* footer */
.footer{position:absolute;left:0;top:2418px;width:1200px;height:398px;background:var(--footer);color:#ccc}
.footer h3{font-size:11px;font-weight:700;letter-spacing:1px;color:#fff;text-transform:uppercase}
.footer .nav{position:absolute;left:40px;top:44px}
.footer .nav a{display:block;color:#aaa;font-size:11px;text-decoration:none;margin-top:10px}
.footer .news{position:absolute;left:600px;top:44px;width:560px}
.footer .news p{font-size:11px;color:#999;margin-top:18px}
.footer form{display:flex;margin-top:12px}
.footer input{flex:1;height:34px;border:0;background:#2a2a2a;color:#888;padding:0 12px;font:11px "Open Sans",sans-serif}
.footer button{width:110px;height:34px;border:0;background:#3a3a3a;color:#ddd;font:600 11px "Open Sans",sans-serif}
.footer .social{position:absolute;left:0;top:236px;width:1200px;display:flex;justify-content:center;gap:12px}
.footer .social span{width:22px;height:22px;background:#3b5998}
.footer .social span+span{background:#4a4a4a}
.footer .legal{position:absolute;left:0;top:320px;width:1200px;text-align:center;font-size:11px;color:#999}
</style>
</head>
<body>
<div class="page">

  <header class="topbar">
    <span class="like"><svg width="10" height="10" viewBox="0 0 10 10"><rect width="10" height="10" fill="#fff" opacity=".8"/></svg>Gefällt mir</span>
    <span>Kostenlose Lieferung · 30 Tage Rückgaberecht</span>
    <span class="tools">
      <svg viewBox="0 0 16 16"><circle cx="7" cy="7" r="5"/><path d="M11 11l4 4"/></svg>
      <svg viewBox="0 0 16 16"><circle cx="8" cy="5" r="3"/><path d="M2 15c1-4 11-4 12 0"/></svg>
      <svg viewBox="0 0 16 16"><path d="M1 2h3l2 9h8l1-6H5"/></svg>
    </span>
  </header>

  <div class="brand">
    <span class="mark"></span>
    <span class="name">VARNOKI</span>
  </div>

  <nav class="mainnav">
    <a href="#" class="active">HOME</a>
    <a href="#">ONLINE SHOP ▾</a>
    <a href="#">ANGEBOT ▾</a>
    <a href="#">VARNOKI ▾</a>
    <a href="#">HILFE GRÖSSE</a>
    <a href="#">KONTAKT</a>
  </nav>

  <section class="hero">
    <div class="photo" role="img" aria-label="Geschäftsmann in dunkelblauem Hemd und heller Hose"></div>
    <div class="copy">
      <h1>EINFACH:</h1>
      <ul>
        <li>Ohne mühsames Anmessen</li>
        <li>Ohne zeitraubende Shoppingtouren</li>
        <li>Jederzeit nachbestellen</li>
      </ul>
      <a class="cta" href="#">Online Shop</a>
    </div>
  </section>

  <section class="category shirts" style="top:838px">
    <h2>HEMDEN</h2>
    <div class="row">
      <svg class="arrow" style="left:-40px;top:100px" viewBox="0 0 20 20"><path d="M13 3L6 10l7 7"/></svg>
      <svg class="arrow" style="right:-40px;top:100px" viewBox="0 0 20 20"><path d="M7 3l7 7-7 7"/></svg>
      <div class="product"><div class="img" role="img" aria-label="Weisses Businesshemd"></div><p class="tag">Tailliert · Ohne Tasche</p><p class="title">Weisses Hemd mit Kentkragen Popeline Art. 1</p><p class="price">ab CHF 79.00 · CHF 99.00</p></div>
      <div class="product"><div class="img blue" role="img" aria-label="Hellblaues Businesshemd"></div><p class="tag">Tailliert · Ohne Tasche</p><p class="title">Hellblaues Hemd mit Haifischkragen Oxford Art. 2</p><p class="price">ab CHF 79.00 · CHF 99.00</p></div>
      <div class="product"><div class="img sky" role="img" aria-label="Hellblau gestreiftes Businesshemd"></div><p class="tag">Tailliert · Ohne Tasche</p><p class="title">Gestreiftes Hemd mit Kentkragen Twill Art. 3</p><p class="price">ab CHF 79.00 · CHF 99.00</p></div>
      <div class="product"><div class="img" role="img" aria-label="Weisses Hemd mit feiner Struktur"></div><p class="tag">Tailliert · Ohne Tasche</p><p class="title">Weisses Hemd mit Button-Down Struktur Art. 4</p><p class="price">ab CHF 79.00 · CHF 99.00</p></div>
      <div class="product"><div class="img sky" role="img" aria-label="Fein kariertes Businesshemd"></div><p class="tag">Tailliert · Ohne Tasche</p><p class="title">Kariertes Hemd mit Haifischkragen Fil-à-Fil Art. 5</p><p class="price">ab CHF 79.00 · CHF 99.00</p></div>
      <div class="product"><div class="img" role="img" aria-label="Weisses Hemd mit Umschlagmanschette"></div><p class="tag">Tailliert · Ohne Tasche</p><p class="title">Weisses Hemd mit Umschlagmanschette Satin Art. 6</p><p class="price">ab CHF 79.00 · CHF 99.00</p></div>
    </div>
  </section>

  <section class="category ties" style="top:1258px">
    <h2>KRAWATTEN &amp; EINSTECKTÜCHER</h2>
    <div class="row">
      <svg class="arrow" style="left:-40px;top:90px" viewBox="0 0 20 20"><path d="M13 3L6 10l7 7"/></svg>
      <svg class="arrow" style="right:-40px;top:90px" viewBox="0 0 20 20"><path d="M7 3l7 7-7 7"/></svg>
      <div class="product"><div class="img" role="img" aria-label="Bordeauxrote Krawatte"><span style="background:#6e1526"></span></div><p class="tag">Krawatte</p><p class="title">Bordeaux Krawatte aus Seide</p><p class="price">CHF 39.00</p></div>
      <div class="product"><div class="img" role="img" aria-label="Dunkelrote Krawatte"><span style="background:#5c1020"></span></div><p class="tag">Krawatte</p><p class="title">Weinrote Krawatte aus Seide</p><p class="price">CHF 39.00</p></div>
      <div class="product"><div class="img sq" role="img" aria-label="Dunkelrotes Einstecktuch"><span style="background:#5a1a24"></span></div><p class="tag">Einstecktuch</p><p class="title">Weinrotes Einstecktuch gepunktet</p><p class="price">CHF 29.00</p></div>
      <div class="product"><div class="img" role="img" aria-label="Königsblaue Krawatte"><span style="background:#1f3fc9"></span></div><p class="tag">Krawatte</p><p class="title">Königsblaue Krawatte aus Seide</p><p class="price">CHF 39.00</p></div>
      <div class="product"><div class="img" role="img" aria-label="Blaue Krawatte"><span style="background:#2449c4"></span></div><p class="tag">Krawatte</p><p class="title">Blaue Krawatte fein gemustert</p><p class="price">CHF 39.00</p></div>
      <div class="product"><div class="img sq" role="img" aria-label="Blaues Einstecktuch"><span style="background:#2448b8"></span></div><p class="tag">Einstecktuch</p><p class="title">Blaues Einstecktuch aus Seide</p><p class="price">CHF 29.00</p></div>
    </div>
  </section>

  <section class="category links" style="top:1666px">
    <h2>MANSCHETTENKNÖPFE</h2>
    <div class="row">
      <svg class="arrow" style="left:-40px;top:25px" viewBox="0 0 20 20"><path d="M13 3L6 10l7 7"/></svg>
      <svg class="arrow" style="right:-40px;top:25px" viewBox="0 0 20 20"><path d="M7 3l7 7-7 7"/></svg>
      <div class="product"><div class="img" role="img" aria-label="Silberne Manschettenknöpfe"></div><p class="tag">Manschettenknöpfe</p><p class="title">Silberne Manschettenknöpfe rund poliert klassisch</p><p class="price">CHF 49.00</p></div>
      <div class="product"><div class="img" role="img" aria-label="Ovale silberne Manschettenknöpfe"></div><p class="tag">Manschettenknöpfe</p><p class="title">Ovale Manschettenknöpfe aus Edelstahl gebürstet</p><p class="price">CHF 49.00</p></div>
      <div class="product"><div class="img" style="background:linear-gradient(90deg,#c4c4c4,#243f9a)" role="img" aria-label="Manschettenknöpfe mit blauem Einsatz"></div><p class="tag">Manschettenknöpfe</p><p class="title">Manschettenknöpfe mit blauem Emaille Einsatz</p><p class="price">CHF 49.00</p></div>
      <div class="product"><div class="img" style="background:linear-gradient(90deg,#c4c4c4,#3a5fc9)" role="img" aria-label="Eckige Manschettenknöpfe blau"></div><p class="tag">Manschettenknöpfe</p><p class="title">Eckige Manschettenknöpfe blau mit Silberrand</p><p class="price">CHF 49.00</p></div>
      <div class="product"><div class="img" style="background:linear-gradient(90deg,#c4c4c4,#e26b3a)" role="img" aria-label="Manschettenknöpfe mit orangem Einsatz"></div><p class="tag">Manschettenknöpfe</p><p class="title">Manschettenknöpfe mit orangem Emaille Einsatz</p><p class="price">CHF 49.00</p></div>
      <div class="product"><div class="img" style="background:linear-gradient(90deg,#c4c4c4,#2a8fd6)" role="img" aria-label="Hellblaue Manschettenknöpfe"></div><p class="tag">Manschettenknöpfe</p><p class="title">Hellblaue Manschettenknöpfe mit Silberrand</p><p class="price">CHF 49.00</p></div>
    </div>
  </section>

  <section class="category belts" style="top:2058px">
    <h2>GÜRTEL</h2>
    <div class="row">
      <svg class="arrow" style="left:-40px;top:30px" viewBox="0 0 20 20"><path d="M13 3L6 10l7 7"/></svg>
      <svg class="arrow" style="right:-40px;top:30px" viewBox="0 0 20 20"><path d="M7 3l7 7-7 7"/></svg>
      <div class="product"><div class="img" style="background:linear-gradient(180deg,#b0784a,#7a4a26)" role="img" aria-label="Hellbrauner Ledergürtel"></div><p class="tag">Gürtel</p><p class="title">Cognac Ledergürtel mit silberner Schnalle</p><p class="price">CHF 69.00</p></div>
      <div class="product"><div class="img" style="background:linear-gradient(180deg,#7a4e33,#4a2c1a)" role="img" aria-label="Dunkelbrauner Ledergürtel"></div><p class="tag">Gürtel</p><p class="title">Dunkelbrauner Ledergürtel mit silberner Schnalle</p><p class="price">CHF 69.00</p></div>
      <div class="product"><div class="img" style="background:linear-gradient(180deg,#3a3a3a,#141414)" role="img" aria-label="Schwarzer Ledergürtel"></div><p class="tag">Gürtel</p><p class="title">Schwarzer Ledergürtel glatt mit Dornschnalle</p><p class="price">CHF 69.00</p></div>
      <div class="product"><div class="img" style="background:linear-gradient(180deg,#333,#111)" role="img" aria-label="Schwarzer Gürtel mit Strukturleder"></div><p class="tag">Gürtel</p><p class="title">Schwarzer Gürtel mit Strukturleder klassisch</p><p class="price">CHF 69.00</p></div>
      <div class="product"><div class="img" style="background:linear-gradient(180deg,#2e2e2e,#0f0f0f)" role="img" aria-label="Schwarzer Wendegürtel"></div><p class="tag">Gürtel</p><p class="title">Schwarzer Wendegürtel mit Plattenschnalle</p><p class="price">CHF 69.00</p></div>
      <div class="product"><div class="img" style="background:linear-gradient(180deg,#2c2c2c,#0e0e0e)" role="img" aria-label="Schwarzer schmaler Ledergürtel"></div><p class="tag">Gürtel</p><p class="title">Schmaler schwarzer Ledergürtel mit Schnalle</p><p class="price">CHF 69.00</p></div>
    </div>
  </section>

  <footer class="footer">
    <div class="nav">
      <h3>Navigation</h3>
      <a href="#">Suche</a>
      <a href="#">Kontakt</a>
      <a href="#">AGB</a>
    </div>
    <div class="news">
      <h3>Bleiben Sie mit uns in Kontakt</h3>
      <p>Abonnieren Sie unseren Newsletter</p>
      <form><input type="text" value="Geben Sie Ihre E-Mail-Adresse ein"><button type="button">Senden</button></form>
    </div>
    <div class="social"><span></span><span></span></div>
    <p class="legal">Varnoki GmbH | Seestrasse 12 | 8002 Zürich | +41 44 000 12 34 | kontakt@varnoki.com</p>
  </footer>

</div>
</body>
</html>
```